8" x 11" One Page Flyer for Fence Installation Company

We are looking to promote our business with a new flyer that would be handed out in person to people or put at their mailbox/door at their homes. The flyer needs to be creative and attention-grabbing. I have attached some of our previous flyers and our website information. Do not call or email regarding the flyer. We want the flyer to look professional but also friendly. One page, NOT folded. You can use images from our website at www.MyBraxtonYard.com or our Facebook page at www.Facebook.com/HollowbrookRailsBKT. We are flexible with what photos you can use but there must be photos of OUR fences on the flyer. More photos specifically can also be provided. Colors need to be suitable for a flyer printed on canary yellow in color paper OR white paper.

Target Market(s)

Homeowners that need a new fence

Industry/Entity Type

Construction

Font styles to use
Sans Serif
Other font styles liked:
• HD Colton

Colors
0054AA
0677BA
7BADD7
CADEEF
E8F1F8
0094D4
00A9DD
6FCCEA
C7EBF8
E9F6FB

Requirements
Must have
• Our fence photos - mostly wood fence photos (different designs), SIZE SHOULD BE LETTER SIZE 8" x 11"
Nice to have
• A nice bible verse featured at the bottom of the flyer.
Should not have
• DO NOT COPY THE WEBSITE FORMAT, I WANT SOMETHING UNIQUE. Other people's fence photos, they must all come from our website or facebook page

```html
<!DOCTYPE html>
<html lang="en">
<head>
<meta charset="utf-8">
<title>Hollowbrook Rails Flyer</title>
<link href="https://fonts.googleapis.com/css2?family=Montserrat:wght@400;500;600;700;800&display=swap" rel="stylesheet">
<style>
  :root{
    --page-bg:#b9bbc0;
    --paper:#f4f5f6;
    --white:#ffffff;
    --ink:#15171c;
    --muted:#5c6068;
    --brand-blue:#1d8ad0;
    --title-blue:#1c8fd3;
    --deep-blue:#2148b0;
    --sky-blue:#0a9ee2;
    --navy:#15234f;
    --tile-1:#29a6e0;
    --tile-2:#188bcb;
    --band-gray:#e7e8eb;
    --rule:#b3b5b9;
    --mark-brown:#5a3b24;
  }
  *{margin:0;padding:0;box-sizing:border-box}
  html,body{width:929px;height:1200px;overflow:hidden;background:var(--page-bg)}
  body{font-family:"Montserrat",sans-serif;color:var(--ink);position:relative}
  .flyer{position:absolute;left:37px;top:0;width:855px;height:1200px;background:var(--paper);overflow:hidden}
  .abs{position:absolute}
  .hero{position:absolute;left:0;top:0;width:855px;height:566px}

  .brand-mark{left:26px;top:28px;width:52px;height:52px;background:var(--mark-brown)}
  .brand-name{left:112px;top:28px;font-weight:700;font-size:22px;color:var(--brand-blue);letter-spacing:.2px;white-space:nowrap}
  .brand-phone{left:112px;top:60px;font-weight:800;font-size:25px;color:var(--ink)}
  .script-word{left:18px;top:150px;width:92px;height:48px;background:#eceef1;border-radius:4px}
  .tagline{left:115px;top:118px;font-weight:700;font-size:22px;line-height:24px;letter-spacing:-.6px;color:var(--ink)}

  .panel-heading{left:48px;top:262px;font-weight:700;font-size:26px;line-height:29.5px;letter-spacing:-.9px;color:var(--white);text-transform:uppercase}
  .panel-quote{left:52px;top:424px;font-weight:700;font-size:13px;line-height:20px;letter-spacing:-.5px;color:var(--white);text-transform:uppercase}

  .invite-bar{left:54px;top:594px;width:5px;height:62px;background:#b0b2b6}
  .invite-title{left:76px;top:594px;font-weight:700;font-size:18px;letter-spacing:-.6px;color:var(--title-blue)}
  .invite-text{left:77px;top:624px;font-size:14.5px;line-height:16px;color:var(--ink)}
  .call-label{left:640px;top:604px;font-size:12.5px;color:var(--white)}
  .call-phone{left:640px;top:622px;font-weight:800;font-size:20px;color:var(--white)}
  .chat-icon{left:582px;top:610px}

  .rule{left:52px;width:753px;height:3px;background:var(--rule)}

  .tile{left:52px;width:89px;height:88px;display:flex;align-items:center;justify-content:center}
  .tile-1{top:742px;background:var(--tile-1)}
  .tile-2{top:830px;background:var(--tile-2)}
  .tile-3{top:918px;background:var(--navy)}
  .service{left:162px;width:290px}
  .service h3{font-weight:700;font-size:17.5px;line-height:22px;letter-spacing:-.4px;color:var(--title-blue);margin-bottom:4px;white-space:nowrap}
  .service p{font-size:11.5px;line-height:15px;color:var(--muted);white-space:nowrap}
  .service.dark h3{color:var(--navy)}
  .service-sep{left:162px;width:248px;height:1px;background:#c5c7cb}

  .why{left:457px;top:742px;width:348px;height:272px;background:var(--white);padding:18px 0 0 26px}
  .why h2{font-weight:700;font-size:17px;line-height:21px;color:var(--title-blue)}
  .why .underline{width:61px;height:3px;background:var(--title-blue);margin:14px 0 10px}
  .why ul{list-style:none}
  .why li{font-size:14.5px;line-height:25.2px;color:var(--ink);letter-spacing:-.2px;white-space:nowrap}
  .why li::before{content:"\203A";margin-right:5px;font-size:17px}

  .foot-address{left:71px;top:1095px;font-weight:700;font-size:17px;letter-spacing:-.5px;color:var(--white)}
  .foot-email{left:515px;top:1096px;font-size:16px;color:var(--white)}
  .foot-icon{left:470px;top:1092px}
</style>
</head>
<body>
<div class="flyer">

  <svg class="hero" viewBox="0 0 855 566">
    <defs>
      <linearGradient id="panelGrad" x1="0" y1="0" x2="1" y2="0.4">
        <stop offset="0" stop-color="#2148b0"/>
        <stop offset="1" stop-color="#05a3e6"/>
      </linearGradient>
      <linearGradient id="woodGrad" x1="0" y1="0" x2="0" y2="1">
        <stop offset="0" stop-color="#8fb26a"/>
        <stop offset="1" stop-color="#c9a46b"/>
      </linearGradient>
    </defs>
    <rect x="200" y="0" width="256" height="566" fill="url(#woodGrad)" role="img" aria-label="Photo of a split rail wooden fence with wire mesh and a company yard sign"/>
    <rect x="462" y="0" width="216" height="566" fill="#b9946a" role="img" aria-label="Photo of a tall wooden privacy fence beside a flower bed"/>
    <rect x="685" y="0" width="170" height="273" fill="#4f7a3c" role="img" aria-label="Photo of a black aluminium fence on a green lawn"/>
    <rect x="685" y="279" width="170" height="287" fill="#cfae73" role="img" aria-label="Photo of a wooden picket fence beside a grey house"/>
    <polygon points="0,0 392,0 240,222 0,222" fill="#ffffff"/>
    <polygon points="392,0 422,0 312,118 280,118" fill="#1d8ad0"/>
    <polygon points="0,222 335,222 635,541 61,541 0,481" fill="url(#panelGrad)"/>
    <polygon points="0,481 61,541 0,541" fill="#f4f5f6"/>
    <polygon points="0,541 635,541 630,566 0,566" fill="#f4f5f6"/>
  </svg>

  <div class="abs brand-mark"></div>
  <div class="abs brand-name">Hollowbrook Rails</div>
  <div class="abs brand-phone">555-014-2290</div>
  <div class="abs script-word" role="img" aria-label="Hand-lettered word: because"></div>
  <div class="abs tagline">Goog Fences<br>Make Good<br>Neighbors</div>

  <div class="abs panel-heading">A growing team<br>of individuals with<br>over 30 years of<br>experience within<br>the fencing industry.</div>
  <div class="abs panel-quote">“And we know that for those who love God all<br>things work together for good, for those who<br>are called according to his purpose”</div>

  <svg class="abs" style="left:0;top:566px" width="855" height="120" viewBox="0 0 855 120">
    <defs>
      <linearGradient id="callGrad" x1="0" y1="0" x2="1" y2="0">
        <stop offset="0" stop-color="#09a0e2"/>
        <stop offset="1" stop-color="#2347b0"/>
      </linearGradient>
    </defs>
    <polygon points="0,0 436,0 548,120 0,120" fill="var(--band-gray)"/>
    <polygon points="465,0 855,0 855,120 577,120" fill="url(#callGrad)"/>
  </svg>
  <div class="abs invite-bar"></div>
  <div class="abs invite-title">We would love to build your fence too!</div>
  <div class="abs invite-text">A growing team of individuals with over 30 years<br>of experience within the fencing industry!</div>
  <svg class="abs chat-icon" width="30" height="30" viewBox="0 0 30 30" fill="none" stroke="#fff" stroke-width="1.8">
    <path d="M3 4h24v16H12l-6 5v-5H3z"/>
    <path d="M8 10h14M8 14h14"/>
  </svg>
  <div class="abs call-label">Call Us Now For Details!</div>
  <div class="abs call-phone">555-014-2290</div>

  <div class="abs rule" style="top:712px"></div>

  <div class="abs tile tile-1">
    <svg width="52" height="40" viewBox="0 0 52 40" fill="none" stroke="#fff" stroke-width="1.8">
      <path d="M2 8h48M2 34h48M2 38h48"/>
      <path d="M5 4v34M12 8v30M19 8v30M26 4v34M33 8v30M40 8v30M47 4v34"/>
    </svg>
  </div>
  <div class="abs tile tile-2">
    <svg width="52" height="40" viewBox="0 0 52 40" fill="none" stroke="#fff" stroke-width="1.8">
      <path d="M2 14h48M2 30h48"/>
      <path d="M6 38V8l3-5 3 5v30M16 38V8l3-5 3 5v30M26 38V8l3-5 3 5v30M36 38V8l3-5 3 5v30M46 38V8l2-4"/>
    </svg>
  </div>
  <div class="abs tile tile-3">
    <svg width="50" height="40" viewBox="0 0 50 40" fill="none" stroke="#fff" stroke-width="1.8">
      <path d="M2 6h46M2 34h46"/>
      <path d="M5 6v32M14 6v32M23 6v32M32 6v32M41 6v32M9 10v22M18 10v22M27 10v22M36 10v22"/>
    </svg>
  </div>

  <div class="abs service" style="top:754px">
    <h3>Almunium Fences</h3>
    <p>Choose among Flat top, Spear top,<br>Flat Top with Spears or Staggered<br>Spear Top Fence styles.</p>
  </div>
  <div class="abs service-sep" style="top:835px"></div>
  <div class="abs service" style="top:842px">
    <h3>Wooden Fences</h3>
    <p>You can choose from a variety of wood<br>fences. privacy Fence or Split Rails or<br>with Estate, Hollowbrook or Dog Ear Privacy.</p>
  </div>
  <div class="abs service-sep" style="top:921px"></div>
  <div class="abs service" style="top:932px">
    <h3>Wooden Trash Enclosures</h3>
    <p>Need an estimate? Call us today to<br>schedule a free estimate at<br>555-014-2290</p>
  </div>

  <div class="abs why">
    <h2>Why Choose Us?</h2>
    <div class="underline"></div>
    <ul>
      <li>Free Estimates</li>
      <li>Concrete in every post</li>
      <li>Professional Installation</li>
      <li>HOA Submission Assistance</li>
      <li>FREE Gate Adjustments for life!</li>
      <li>Experienced Installation Teams</li>
      <li>Lifetime Workmanship Warranty</li>
      <li>Quality Workmanship &amp; Materials</li>
    </ul>
  </div>

  <div class="abs rule" style="top:1035px"></div>

  <svg class="abs" style="left:0;top:1060px" width="855" height="92" viewBox="0 0 855 92">
    <defs>
      <linearGradient id="footGrad" x1="0" y1="0" x2="1" y2="0">
        <stop offset="0" stop-color="#2246b0"/>
        <stop offset="1" stop-color="#0a95dc"/>
      </linearGradient>
    </defs>
    <polygon points="24,19 430,19 400,73 12,73" fill="var(--navy)"/>
    <polygon points="427,4 844,4 790,88 375,88" fill="url(#footGrad)"/>
  </svg>
  <div class="abs foot-address">418 Quarry Ln, Braxton NC 28000</div>
  <svg class="abs foot-icon" width="34" height="30" viewBox="0 0 34 30" fill="none" stroke="#fff" stroke-width="1.8">
    <rect x="2" y="2" width="30" height="19" rx="1"/>
    <path d="M17 21v5M10 27h14"/>
  </svg>
  <div class="abs foot-email">office@mybraxtonyard.com</div>

</div>
</body>
</html>
```